Business card design for Bront Engineering Qavo

We need a new business card design along with all the necessary to place an order. The company is Bront Engineering Qavo and we recently updated our logo.

```html
<!DOCTYPE html>
<html lang="en">
<head>
<meta charset="UTF-8">
<title>Bront Engineering Qavo — Business Card</title>
<link rel="stylesheet" href="https://fonts.googleapis.com/css2?family=Montserrat:wght@400;500;600&display=swap">
<style>
  :root {
    --backdrop: #3b3b3d;
    --paper: #ffffff;
    --ink: #1a1a1a;
    --brand-yellow: #e5b900;
    --brand-grey: #9c9899;
    --brand-light: #cfcdcd;
    --card-black: #1d1d1e;
    --pattern-black: #181818;
  }
  * { box-sizing: border-box; margin: 0; padding: 0; }
  html, body {
    width: 1200px; height: 1200px; overflow: hidden;
    background: var(--backdrop);
    font-family: "Montserrat", sans-serif;
  }
  .stage {
    width: 1200px; height: 1200px;
    display: flex; flex-direction: column; align-items: center; justify-content: center;
    gap: 60px;
  }
  .card {
    position: relative;
    width: 840px; height: 480px;
    border-radius: 36px;
    overflow: hidden;
  }
  /* Front */
  .card-front { background: var(--paper); }
  .person {
    position: absolute; left: 64px; top: 150px;
  }
  .person-name {
    font-weight: 600; font-size: 50px; line-height: 1;
    color: var(--brand-yellow); letter-spacing: 0.5px;
    white-space: nowrap;
  }
  .person-role {
    margin-top: 8px;
    font-weight: 400; font-size: 26px; color: var(--ink); letter-spacing: 0.5px;
  }
  .contacts {
    position: absolute; left: 64px; top: 262px;
    list-style: none;
    font-size: 21px; color: var(--ink); line-height: 1.2;
  }
  .contacts li { display: flex; align-items: flex-start; gap: 14px; margin-bottom: 6px; }
  .contacts svg { width: 22px; height: 22px; flex: none; margin-top: 2px; fill: var(--brand-yellow); }

  .brand-name {
    position: absolute;
    display: flex; align-items: center; gap: 14px;
    font-weight: 600; letter-spacing: 2px; line-height: 1.2;
    color: var(--brand-grey);
  }
  .brand-name-text { display: flex; flex-direction: column; white-space: nowrap; }
  .brand-mark { width: 22px; height: 22px; background: var(--brand-yellow); flex: none; }
  .card-front .brand-name { left: 440px; top: 96px; font-size: 26px; }

  .band-yellow {
    position: absolute; left: 0; bottom: 0;
    width: 560px; height: 30px; background: var(--brand-yellow);
  }
  .band-grey {
    position: absolute; right: 0; bottom: 0;
    width: 262px; height: 62px; background: var(--brand-grey);
  }
  /* Back */
  .card-back {
    background: var(--card-black);
    border-bottom: 4px solid var(--brand-yellow);
  }
  .back-pattern {
    position: absolute; inset: 0;
    background: linear-gradient(135deg, var(--card-black), var(--pattern-black));
  }
  .card-back .brand-name {
    left: 500px; top: 250px;
    font-size: 20px; gap: 10px;
    color: var(--brand-light);
  }
  .card-back .brand-mark { width: 16px; height: 16px; }
</style>
</head>
<body>
<main class="stage">
  <section class="card card-front">
    <div class="person">
      <h1 class="person-name">FULL NAME</h1>
      <p class="person-role">POSITION</p>
    </div>
    <ul class="contacts">
      <li>
        <svg viewBox="0 0 24 24"><path d="M6.6 10.8a15.1 15.1 0 0 0 6.6 6.6l2.2-2.2a1 1 0 0 1 1-.25 11.4 11.4 0 0 0 3.6.57 1 1 0 0 1 1 1V20a1 1 0 0 1-1 1A17 17 0 0 1 3 4a1 1 0 0 1 1-1h3.5a1 1 0 0 1 1 1c0 1.25.2 2.45.57 3.57a1 1 0 0 1-.25 1z"/></svg>
        <span>(000) 000 0000</span>
      </li>
      <li>
        <svg viewBox="0 0 24 24"><path d="M2 5h20v14H2z M3.5 6.5 12 13l8.5-6.5" stroke="#fff" stroke-width="1.4"/></svg>
        <span>email@company.com</span>
      </li>
      <li>
        <svg viewBox="0 0 24 24"><circle cx="12" cy="12" r="9.5" fill="none" stroke="#e5b900" stroke-width="1.8"/><path d="M2.5 12h19M12 2.5c-3 3-3 16 0 19M12 2.5c3 3 3 16 0 19" fill="none" stroke="#e5b900" stroke-width="1.5"/></svg>
        <span>www.company.com</span>
      </li>
      <li>
        <svg viewBox="0 0 24 24"><path d="M12 2a7 7 0 0 0-7 7c0 5.2 7 13 7 13s7-7.8 7-13a7 7 0 0 0-7-7zm0 9.5A2.5 2.5 0 1 1 12 6.5a2.5 2.5 0 0 1 0 5z"/></svg>
        <span>123 Name Street, 000<br>Your City, 00000-000</span>
      </li>
    </ul>
    <div class="brand-name">
      <span class="brand-mark"></span>
      <span class="brand-name-text"><span>BRONT ENGINEERING</span><span>QAVO</span></span>
    </div>
    <div class="band-yellow"></div>
    <div class="band-grey"></div>
  </section>

  <section class="card card-back">
    <div class="back-pattern" role="img" aria-label="Embossed repeating brand pattern on black stock"></div>
    <div class="brand-name">
      <span class="brand-mark"></span>
      <span class="brand-name-text"><span>BRONT ENGINEERING</span><span>QAVO</span></span>
    </div>
  </section>
</main>
</body>
</html>
```